Network platform mobile app for professional bussines crd

need my buz card to have all the attached information. (feel free to change the layout )
The key is when ppl see the card , it should feel like it's a screen shot from a cellphone
I want ppl know without asking that my buz is a mobile app.
Reason: no logo on my business cards
Industry/Entity Type
It Professional
Contact Information for Business Card
See attached screen shot. I NEED A DESIGN THAT IS VERY DIFFERENT THAN THIS ONE .
Requirements
Must have
- Besides the personal info and QR , it must feel and look like it's a mobile app from a cell phone and a saved space for my logo
Nice to have
- Like the upper screen some status bars such as wifi signal, likes , etc

```html
<!DOCTYPE html>
<html lang="en">
<head>
<meta charset="utf-8">
<title>Lena Moray – Business Card</title>
<link rel="stylesheet" href="https://fonts.googleapis.com/css2?family=Open+Sans:wght@400;600;700&family=Noto+Serif:wght@400&display=swap">
<style>
  :root {
    --backdrop: #3a3a3c;
    --device-white: #ffffff;
    --device-edge: #e4e4e4;
    --screen-dark: #232323;
    --screen-sheen: #8c8c8c;
    --screen-light: #e6e6e6;
    --brand-blue: #2f9be0;
    --text-grey: #b9b9b9;
    --text-white: #ffffff;
    --tagline-grey: #6b6b6b;
    --button-ring: #d6d6d6;
  }
  * { box-sizing: border-box; margin: 0; padding: 0; }
  html, body {
    width: 1200px; height: 900px; overflow: hidden;
    background: var(--backdrop);
    font-family: "Open Sans", Arial, sans-serif;
  }
  .canvas {
    position: relative; width: 1200px; height: 900px;
    display: flex; justify-content: center; align-items: center; gap: 70px;
  }
  .card {
    position: relative; width: 380px; height: 740px;
    background: var(--device-white);
    border-radius: 52px;
    box-shadow: 0 0 0 1px var(--device-edge);
    overflow: hidden;
  }
  /* front: phone face */
  .card-front .camera {
    position: absolute; top: 40px; left: 50%; width: 12px; height: 12px;
    margin-left: -6px; border-radius: 50%; background: var(--screen-dark);
  }
  .card-front .speaker {
    position: absolute; top: 62px; left: 50%; width: 74px; height: 8px;
    margin-left: -37px; border-radius: 4px; background: var(--screen-dark);
  }
  .card-front .front-dot {
    position: absolute; top: 63px; left: 108px; width: 8px; height: 8px;
    border-radius: 50%; background: var(--screen-dark);
  }
  .card-front .screen {
    position: absolute; top: 118px; left: 22px; right: 22px; height: 514px;
    background: var(--screen-dark); overflow: hidden;
  }
  .screen .sheen { position: absolute; inset: 0; width: 100%; height: 100%; }
  .home-button {
    position: absolute; bottom: 34px; left: 50%; width: 62px; height: 62px;
    margin-left: -31px; border-radius: 50%;
    border: 2px solid var(--button-ring); background: var(--device-white);
  }
  .home-button::after {
    content: ""; position: absolute; top: 50%; left: 50%;
    width: 20px; height: 20px; margin: -10px 0 0 -10px;
    border: 2px solid var(--button-ring); border-radius: 5px;
  }
  .brand-mark {
    position: absolute; left: 0; right: 0;
    display: flex; justify-content: center; align-items: center; gap: 10px;
    font-weight: 600; color: var(--brand-blue); letter-spacing: 2px;
  }
  .brand-mark .dot {
    width: 14px; height: 14px; border-radius: 50%; background: var(--brand-blue);
  }
  .card-front .brand-mark { top: 150px; font-size: 26px; }
  .contact {
    position: absolute; top: 250px; left: 0; right: 0; text-align: center;
  }
  .contact .name {
    font-size: 34px; font-weight: 700; color: var(--brand-blue); letter-spacing: 1px;
  }
  .contact .role {
    font-size: 20px; color: var(--text-grey); margin-top: 2px;
  }
  .contact .phone, .contact .email {
    font-size: 19px; color: var(--text-white);
  }
  .contact .phone { margin-top: 40px; }
  .contact .email { margin-top: 8px; }
  /* back: light screen */
  .card-back .screen {
    position: absolute; top: 56px; left: 0; right: 0; height: 628px;
    background: var(--screen-light);
  }
  .tagline {
    position: absolute; top: 90px; left: 0; right: 0; text-align: center;
    font-family: "Noto Serif", Georgia, serif; font-size: 19px; line-height: 1.2;
    color: var(--tagline-grey);
  }
  .card-back .brand-mark { top: 340px; font-size: 32px; }
</style>
</head>
<body>
<main class="canvas">
  <section class="card card-front" aria-label="Card front">
    <span class="camera"></span>
    <span class="front-dot"></span>
    <span class="speaker"></span>
    <div class="screen">
      <svg class="sheen" viewBox="0 0 336 514" preserveAspectRatio="none" aria-hidden="true">
        <defs>
          <linearGradient id="sheen-fill" x1="0" y1="0" x2="1" y2="1">
            <stop offset="0" stop-color="#6f6f6f"/>
            <stop offset="1" stop-color="#a4a4a4"/>
          </linearGradient>
        </defs>
        <polygon points="150,0 336,0 336,250" fill="url(#sheen-fill)"/>
      </svg>
      <div class="brand-mark"><span class="dot"></span>LINKWAVE</div>
      <div class="contact">
        <p class="name">Lena Moray</p>
        <p class="role">Founder</p>
        <p class="phone">310-555-0142</p>
        <p class="email">hello@linkwaveapp.com</p>
      </div>
    </div>
    <span class="home-button"></span>
  </section>

  <section class="card card-back" aria-label="Card back">
    <div class="screen">
      <p class="tagline">Reshaping ideas with<br>like minded people</p>
      <div class="brand-mark"><span class="dot"></span>LINKWAVE</div>
    </div>
  </section>
</main>
</body>
</html>
```